new incubator startup Plattform

I need a flyer for a business presentation.
Please insert the text ideas from following the attachment.

We are a new incubator, accelerator and co working space for startups. The innovation platform that unites global companies with high tech expertise and the best of Austrian knowhow. Our focus is in AI, Blockchain and e-commerce.
We are a neutral platform moderating an in-depth and curated collaboration between our partners from the industry and young tech companies. Our network of investment firms and mentors further helps the growth of tech companies. Our home is Vienna, a hub of business, engineering, and groundbreaking inventions.

Focus:
AI, Blockchain, e-commerce

Cases
Startup Idea
You have a disruptive idea that needs an accelerator/incubator program

Business Challenge
You want to solve an business problem but do not own an idea

Mature startup Idea
You Have a Disruptive idea that needs a direct commercialization

Benefits
Market and Investor Acces
Direct access to all Partners

Training and Tools

Mentor and Network Muscle
We can link you to many domains like Sales, Marketing, Aftersales, IT und HR.
Experiences Senior and University mentors.
With all Partners as your first potential customer.

```html
<!DOCTYPE html>
<html lang="en">
<head>
<meta charset="utf-8">
<title>New Incubator Startup Plattform – Flyer</title>
<link href="https://fonts.googleapis.com/css2?family=Montserrat:wght@400;600;700&family=Nunito+Sans:wght@400;600;700;800&display=swap" rel="stylesheet">
<style>
  :root {
    --stage: #e4e6ea;
    --paper: #ffffff;
    --navy: #0b0f3a;
    --navy-deep: #060824;
    --blue: #1a9ad9;
    --blue-light: #2fb3ef;
    --ink: #2b2b2b;
    --ink-soft: #444a52;
    --rule: #555;
  }
  * { margin: 0; padding: 0; box-sizing: border-box; }
  html, body { width: 1200px; height: 650px; overflow: hidden; }
  body {
    background: var(--stage);
    font-family: "Nunito Sans", Arial, sans-serif;
    color: var(--ink);
    position: relative;
  }
  .flyer {
    position: absolute; left: 381px; top: 15px;
    width: 438px; height: 620px;
    background: var(--paper);
    overflow: hidden;
    box-shadow: 0 6px 18px rgba(0,0,0,.18);
  }
  .hero {
    position: absolute; left: 0; top: 0; width: 438px; height: 250px;
    background: radial-gradient(circle at 38% 62%, #2d6fd6 0%, #143a8a 22%, var(--navy) 55%, var(--navy-deep) 100%);
  }
  .hero-accent {
    position: absolute; top: 0; right: 16px; width: 160px; height: 7px; background: var(--blue);
  }
  .rocket-art {
    position: absolute; left: 70px; top: 30px; width: 140px; height: 210px;
    background: linear-gradient(160deg, #c9cbd6 0%, #7b7f96 45%, rgba(240,150,60,.6) 80%, rgba(255,230,170,0) 100%);
    border-radius: 60px 60px 20px 20px;
    opacity: .85;
  }
  .headline {
    position: absolute; right: 28px; top: 34px; text-align: left;
    font-family: "Montserrat", Arial, sans-serif; color: #fff; line-height: 1;
  }
  .headline .kicker { font-size: 17px; font-weight: 400; letter-spacing: .2px; }
  .headline .kicker b { color: var(--blue-light); font-weight: 600; }
  .headline .main { font-size: 42px; font-weight: 700; letter-spacing: -1px; margin-top: 4px; }
  .headline .sub { font-size: 31px; font-weight: 600; color: var(--blue-light); margin-top: 3px; letter-spacing: .2px; }
  .monitor {
    position: absolute; left: 248px; top: 141px; width: 166px; height: 113px;
    background: #cfd3da; border-radius: 4px; padding: 5px 5px 14px;
  }
  .monitor-screen {
    width: 100%; height: 100%;
    background: linear-gradient(135deg, #e8eef6 0%, #7aa6d8 45%, #2c5da8 100%);
  }
  .monitor-stand {
    position: absolute; left: 318px; top: 254px; width: 26px; height: 14px; background: #b8bcc4;
  }
  .tagline-band {
    position: absolute; left: 0; top: 250px; width: 438px; height: 41px;
    background: var(--blue); color: #fff;
    font-size: 10.2px; font-weight: 600; line-height: 1.3;
    padding: 7px 0 0 24px;
  }
  .focus { position: absolute; left: 0; top: 300px; width: 438px; height: 90px; }
  .focus-item {
    position: absolute; width: 110px; text-align: center;
    font-family: "Montserrat", Arial, sans-serif; font-size: 9px; font-weight: 600; line-height: 1.2;
    text-transform: uppercase; color: var(--ink);
  }
  .focus-item svg { display: block; margin: 0 auto 8px; }
  .focus-arrow { position: absolute; top: 25px; }
  .cases { position: absolute; top: 405px; width: 200px; }
  .cases-left { left: 20px; }
  .cases-right { left: 231px; width: 205px; }
  .case { position: relative; padding-left: 16px; margin-bottom: 9px; }
  .case svg { position: absolute; left: 0; top: 1px; }
  .case h3 {
    font-size: 8.4px; font-weight: 700; color: var(--blue); text-transform: uppercase; letter-spacing: .2px;
  }
  .case p { font-size: 8px; line-height: 1.3; color: var(--ink-soft); }
  .divider { position: absolute; left: 219px; top: 402px; width: 1px; height: 117px; background: var(--rule); }
  .about {
    position: absolute; left: 24px; top: 528px; width: 400px;
    font-size: 7.8px; line-height: 1.36; color: var(--ink-soft);
  }
  .about strong { color: var(--blue); font-weight: 700; }
  .footer-band {
    position: absolute; left: 0; top: 572px; width: 438px; height: 35px; background: var(--blue);
  }
  .web-pill {
    position: absolute; left: 57px; top: 582px; width: 116px; height: 15px;
    border: 1px solid #fff; border-radius: 8px;
    color: #fff; font-size: 7px; font-weight: 600; text-align: center; line-height: 13px;
  }
  .brand-plate {
    position: absolute; left: 208px; top: 566px; width: 240px; height: 47px;
    background: #fff; border-radius: 24px 0 0 24px;
  }
  .brand-name {
    position: absolute; left: 250px; top: 572px;
    font-size: 27px; font-weight: 800; color: var(--ink-soft); letter-spacing: -.5px;
  }
</style>
</head>
<body>
  <main class="flyer">
    <section class="hero">
      <div class="hero-accent"></div>
      <div class="rocket-art" role="img" aria-label="Illustration of a rocket launching over a glowing blue circuit background"></div>
      <h1 class="headline">
        <div class="kicker">NEW <b>INCUBATOR</b></div>
        <div class="main">STARTUP</div>
        <div class="sub">PLATTFORM</div>
      </h1>
      <div class="monitor"><div class="monitor-screen" role="img" aria-label="Photo of a keyboard with a shopping basket and pointer on the screen"></div></div>
      <div class="monitor-stand"></div>
    </section>

    <p class="tagline-band">The innovation platform that unites global companies<br>with high tech expertise and the best of Austrian know how.</p>

    <section class="focus">
      <div class="focus-item" style="left:28px">
        <svg width="52" height="52" viewBox="0 0 52 52"><circle cx="26" cy="26" r="25" fill="#1a9ad9"/>
          <g fill="none" stroke="#fff" stroke-width="1.4"><rect x="18" y="18" width="16" height="16" rx="2"/><rect x="22" y="22" width="8" height="8"/>
          <path d="M21 18v-5M26 18v-5M31 18v-5M21 34v5M26 34v5M31 34v5M18 21h-5M18 26h-5M18 31h-5M34 21h5M34 26h5M34 31h5"/></g></svg>
        Artificial<br>Intelligence
      </div>
      <svg class="focus-arrow" style="left:110px" width="72" height="22" viewBox="0 0 72 22"><path d="M2 12 Q36 -2 66 14" fill="none" stroke="#222" stroke-width="1.3"/><path d="M60 9 L67 15 L58 17" fill="none" stroke="#222" stroke-width="1.3"/></svg>
      <div class="focus-item" style="left:163px">
        <svg width="52" height="52" viewBox="0 0 52 52"><circle cx="26" cy="26" r="25" fill="#1a9ad9"/>
          <g fill="none" stroke="#fff" stroke-width="1.4"><polygon points="26,17 34,21.5 34,30.5 26,35 18,30.5 18,21.5"/>
          <circle cx="26" cy="11" r="2.5"/><circle cx="39" cy="18" r="2.5"/><circle cx="39" cy="34" r="2.5"/><circle cx="26" cy="41" r="2.5"/><circle cx="13" cy="34" r="2.5"/><circle cx="13" cy="18" r="2.5"/>
          <path d="M26 13.5V17M37 19.5L34 21.5M37 32.5L34 30.5M26 38.5V35M15 32.5L18 30.5M15 19.5L18 21.5"/></g></svg>
        Blockchain<br>Technology
      </div>
      <svg class="focus-arrow" style="left:242px" width="72" height="22" viewBox="0 0 72 22"><path d="M2 14 Q36 26 66 6" fill="none" stroke="#222" stroke-width="1.3"/><path d="M58 5 L67 5 L63 13" fill="none" stroke="#222" stroke-width="1.3"/></svg>
      <div class="focus-item" style="left:291px">
        <svg width="52" height="52" viewBox="0 0 52 52"><circle cx="26" cy="26" r="25" fill="#1a9ad9"/>
          <g fill="none" stroke="#fff" stroke-width="1.4"><circle cx="24" cy="24" r="11"/><ellipse cx="24" cy="24" rx="5" ry="11"/><path d="M13 24h22M15 18h18M15 30h18"/>
          <path d="M29 31h3l2 7h8l2-5h-11"/><circle cx="35" cy="40" r="1"/><circle cx="41" cy="40" r="1"/></g></svg>
        E-Commerce<br>Technology
      </div>
    </section>

    <section class="cases cases-left">
      <div class="case"><svg width="10" height="10" viewBox="0 0 10 10"><rect x=".5" y="1.5" width="8" height="8" fill="none" stroke="#1a9ad9"/><path d="M2 5l2 2 5-6" fill="none" stroke="#1a9ad9" stroke-width="1.3"/></svg>
        <h3>Startup Idea</h3><p>You have a disruptive idea that needs an<br>accelerator/incubator program</p></div>
      <div class="case"><svg width="10" height="10" viewBox="0 0 10 10"><rect x=".5" y="1.5" width="8" height="8" fill="none" stroke="#1a9ad9"/><path d="M2 5l2 2 5-6" fill="none" stroke="#1a9ad9" stroke-width="1.3"/></svg>
        <h3>Business Challenge</h3><p>You want to solve an business problem but<br>do not own an idea</p></div>
      <div class="case"><svg width="10" height="10" viewBox="0 0 10 10"><rect x=".5" y="1.5" width="8" height="8" fill="none" stroke="#1a9ad9"/><path d="M2 5l2 2 5-6" fill="none" stroke="#1a9ad9" stroke-width="1.3"/></svg>
        <h3>Mature Startup Idea</h3><p>You Have a Disruptive idea that needs a<br>direct commercialization</p></div>
    </section>

    <div class="divider"></div>

    <section class="cases cases-right">
      <div class="case"><svg width="10" height="10" viewBox="0 0 10 10"><rect x=".5" y="1.5" width="8" height="8" fill="none" stroke="#1a9ad9"/><path d="M2 5l2 2 5-6" fill="none" stroke="#1a9ad9" stroke-width="1.3"/></svg>
        <h3>Benefits</h3><p>Market and Investor Acces<br>Direct access to all Partners</p></div>
      <div class="case"><svg width="10" height="10" viewBox="0 0 10 10"><rect x=".5" y="1.5" width="8" height="8" fill="none" stroke="#1a9ad9"/><path d="M2 5l2 2 5-6" fill="none" stroke="#1a9ad9" stroke-width="1.3"/></svg>
        <h3>Training and Tools</h3></div>
      <div class="case"><svg width="10" height="10" viewBox="0 0 10 10" style="top:12px"><rect x=".5" y="1.5" width="8" height="8" fill="none" stroke="#1a9ad9"/><path d="M2 5l2 2 5-6" fill="none" stroke="#1a9ad9" stroke-width="1.3"/></svg>
        <h3>Mentor and Network Muscle</h3><p>We can link you to many domains like Sales,<br>Marketing, Aftersales, IT und HR.<br>Experiences Senior and University mentors.<br>With all Partners as your first potential customer.</p></div>
    </section>

    <p class="about">We are a neutral platform moderating an in-depth and curated collaboration between our partners from the industry and young tech companies. Our network of investment firms and mentors further helps the growth of tech companies. <strong>Our home is Vienna, a hub of business, engineering, and groundbreaking inventions.</strong></p>

    <footer>
      <div class="footer-band"></div>
      <div class="web-pill">www.novalaunch-hub.com</div>
      <div class="brand-plate"></div>
      <div class="brand-name">Novalaunch</div>
    </footer>
  </main>
</body>
</html>
```